Tri-fold flyer for Wanderlodge Hostel

We would like a new tri fold flyer for our hostel. We've opened up a new location called "Tidecourt", and the details and photos of the location can be found at: http://www.palmrestlodging.com.au/locations/tidecourt/
rooms_and_facilities.html. If you have particular types of photos you would like to use we also have a large stock of photos from around the area that we can dig through and make available upon request.
A copy of an old brochure for a different location can be found at: http://www.palmrestlodging.com.au/marketing/PRL_Tri-fold_Brochure.pdf, however we would like a new design from the ground up.
The flyer should convey a more upmarket image, so it should remain classy/classic - not too "busy" looking, but not boring either. Very chic.
The basic colours must be Purple/Silver/Black. The purple is actually a very specific colour but I assume you can get this from the PDF (otherwise there is an Illustrator file available at http://www.palmrestlodging.com.au/marketing/PRL_Tri-fold_Brochure.indd). Also, a large version of the logo can be found at http://www.palmrestlodging.com.au/marketing/logo_source.png if you need it.
Finally, it's important that guests can easily find us so other than the logo a map is about the only absolutely essential element. There is a Google Maps image on our web-site (http://www.palmrestlodging.com.au/locations/tidecourt/contact.html) that explains where we are, but we're sure that this can't be copied to to the flyer for copyright reasons. We would prefer a simpler map anyway.
The important landmarks are:
*Our hostel
*Roadkestrel bus and Corvel Island ferry terminal
*Staveline bus terminal
*Murrow Knoll
*Tallis Gardens
*Pellingham Marina
*The Parade
*Wyatt Creek
The important streets are:
*The Parade
*Calloway Street
*Harland Street
*Morrow Street
*Tuck/Ambry/Vale Streets (One road, it just changes names)
*Quill Street
(Note: The Parade refers to a street and a long beach frontage)
I have created a Google Maps map with all of these points labelled:
https://maps.examplemapsite.com.au/maps/ms?
msid=000000000000000000000.0000a000a0a000a00000a&
msa=0&ll=-00.000000,000.000000&
spn=0.00000,0.000000
Target Market(s)
Backpackers, students, short-term residents and seasonal workers

```html
<!DOCTYPE html>
<html lang="en">
<head>
<meta charset="utf-8">
<title>Palm Rest Lodging Tidecourt – Rooms &amp; Facilities</title>
<link rel="stylesheet" href="https://fonts.googleapis.com/css2?family=Sorts+Mill+Goudy&family=Cabin:wght@400;600&display=swap">
<style>
  :root {
    --plum: #8a4650;
    --plum-soft: #c9a3a8;
    --ink: #1c1c1c;
    --sheet: #f5f5f7;
    --panel: #fbfbfc;
    --edge: #cfcfd4;
    --page: #ffffff;
  }
  * { margin: 0; padding: 0; box-sizing: border-box; }
  html, body { width: 1200px; height: 900px; overflow: hidden; background: var(--page); }
  body { font-family: "Cabin", sans-serif; color: var(--ink); font-size: 12px; line-height: 16px; }

  .spread { position: absolute; left: 35px; top: 50px; width: 1122px; height: 793px;
    background: var(--sheet); border: 1px solid var(--edge); overflow: hidden; }
  .panel-right { position: absolute; left: 748px; top: 0; width: 374px; height: 100%; background: var(--panel); }

  .photo { position: absolute; display: block; }
  .photo-lounge { left: 0; top: 0; }
  .photo-dorm { left: 748px; top: 600px; }

  .abs { position: absolute; }
  .heading { font-family: "Sorts Mill Goudy", serif; color: var(--plum); font-weight: 400; }
  .heading-main { font-size: 24px; line-height: 30px; letter-spacing: -0.3px; }
  .heading-sub { font-size: 18px; line-height: 22px; }
  .flourish { position: absolute; width: 84px; height: 10px; border-radius: 5px;
    background: linear-gradient(90deg, transparent, var(--plum-soft), transparent); }
  .lead { font-weight: 600; font-size: 12px; line-height: 16px; }
  .rule-strong { position: absolute; height: 3px; background: var(--plum); opacity: .85; }
  .rule-thin { position: absolute; height: 1px; background: #555; }

  .col-head { position: absolute; font-weight: 600; }
  .cell { position: absolute; white-space: nowrap; }
  .note { position: absolute; color: var(--plum); font-size: 10px; line-height: 16px; }
  .note sup { font-size: 9px; }

  .features { position: absolute; left: 783px; top: 227px; list-style: none; width: 320px; }
  .features li { position: relative; padding-left: 12px; }
  .features li::before { content: "•"; position: absolute; left: 0; }
  .features sup { font-size: 8px; line-height: 0; }
</style>
</head>
<body>
<main class="spread">
  <div class="panel-right"></div>

  <svg class="photo photo-lounge" width="748" height="262" viewBox="0 0 748 262" role="img" aria-label="Photo of the hostel common room with a row of computer desks against purple walls">
    <defs>
      <linearGradient id="loungeTone" x1="0" y1="0" x2="1" y2="0.4">
        <stop offset="0" stop-color="#b98a6a"/>
        <stop offset="0.35" stop-color="#8e3f86"/>
        <stop offset="0.7" stop-color="#b77fb3"/>
        <stop offset="1" stop-color="#e9e7ea"/>
      </linearGradient>
    </defs>
    <path d="M0 0 H748 V196 C700 238 620 256 520 255 C400 254 300 226 200 212 C120 202 50 202 0 210 Z" fill="url(#loungeTone)"/>
    <path d="M0 210 C50 202 120 202 200 212 C300 226 400 254 520 255 C620 256 700 238 748 196" fill="none" stroke="#fff" stroke-width="3" opacity=".9"/>
    <path d="M0 192 C80 180 180 186 290 204 C400 222 520 236 620 222 C680 212 720 196 748 176" fill="none" stroke="#fff" stroke-width="2" opacity=".55"/>
    <path d="M0 178 C90 164 190 172 300 188 C410 204 530 216 630 202 C690 192 725 176 748 160" fill="none" stroke="#fff" stroke-width="1.5" opacity=".35"/>
  </svg>

  <svg class="photo photo-dorm" width="374" height="193" viewBox="0 0 374 193" role="img" aria-label="Photo of a bright dorm room with bunk beds and a desk">
    <defs>
      <linearGradient id="dormTone" x1="0" y1="0" x2="0" y2="1">
        <stop offset="0" stop-color="#f3eddb"/>
        <stop offset="0.55" stop-color="#e4d8bf"/>
        <stop offset="1" stop-color="#c86b62"/>
      </linearGradient>
    </defs>
    <path d="M0 46 C90 22 200 30 280 14 C320 6 350 4 374 6 V193 H0 Z" fill="url(#dormTone)"/>
    <path d="M0 46 C90 22 200 30 280 14 C320 6 350 4 374 6" fill="none" stroke="#fff" stroke-width="3"/>
    <path d="M0 58 C100 34 210 44 290 26 C330 18 356 16 374 18" fill="none" stroke="#fff" stroke-width="1.5" opacity=".6"/>
  </svg>

  <!-- Rooms panel -->
  <h1 class="abs heading heading-main" style="left:0;width:404px;top:218px;text-align:center;">Rooms</h1>
  <span class="flourish" style="left:160px;top:251px;" role="img" aria-label="Decorative flourish"></span>
  <p class="abs lead" style="left:47px;top:275px;width:330px;">Palm Rest Lodging Tidecourt has a range of spacious dorm and private rooms available year round</p>
  <div class="rule-strong" style="left:47px;top:317px;width:668px;"></div>

  <h2 class="abs heading heading-sub" style="left:47px;top:335px;">Dorm Rooms</h2>
  <div class="rule-thin" style="left:47px;top:366px;width:310px;"></div>
  <span class="col-head" style="left:47px;top:375px;">Room type</span>
  <span class="col-head" style="left:156px;top:375px;">Facilities</span>
  <span class="col-head" style="left:264px;top:375px;">Price</span>
  <div class="rule-thin" style="left:47px;top:397px;width:310px;"></div>

  <span class="cell" style="left:47px;top:419px;">8-bed dorm<br>(mixed)</span>
  <span class="cell" style="left:156px;top:419px;">Bunk beds<br>Air conditioning</span>
  <span class="cell" style="left:264px;top:419px;">From $24 per<br>person per night</span>

  <span class="cell" style="left:47px;top:467px;">6-bed dorm<br>(mixed)</span>
  <span class="cell" style="left:156px;top:467px;">Bunk beds<br>Air conditioning</span>
  <span class="cell" style="left:264px;top:467px;">From $25 per<br>person per night</span>

  <span class="cell" style="left:47px;top:515px;">4-bed dorm<br>(mixed)</span>
  <span class="cell" style="left:156px;top:515px;">Bunk beds<br>Air conditioning</span>
  <span class="cell" style="left:264px;top:515px;">From $27 per<br>person per night</span>

  <span class="cell" style="left:47px;top:563px;">4-bed dorm<br>(female only)</span>
  <span class="cell" style="left:156px;top:563px;">Bunk beds<br>Air conditioning<br>Balcony<br>Ensuite</span>
  <span class="cell" style="left:264px;top:563px;">From $27 per<br>person per night</span>

  <p class="note" style="left:47px;top:707px;width:310px;"><sup>*</sup> Please contact us regarding availability. Weekly and monthly rates are<br>&nbsp;&nbsp;also available for all room types upon request.</p>

  <h2 class="abs heading heading-sub" style="left:405px;top:335px;">Private Rooms</h2>
  <div class="rule-thin" style="left:405px;top:366px;width:310px;"></div>
  <span class="col-head" style="left:405px;top:375px;">Room type</span>
  <span class="col-head" style="left:514px;top:375px;">Facilities</span>
  <span class="col-head" style="left:623px;top:375px;">Price</span>
  <div class="rule-thin" style="left:405px;top:397px;width:310px;"></div>

  <span class="cell" style="left:405px;top:419px;">Single</span>
  <span class="cell" style="left:514px;top:419px;">Single bed<br>Personal kitchen<br>locker</span>
  <span class="cell" style="left:623px;top:419px;">From $50 per<br>person per night</span>

  <span class="cell" style="left:405px;top:483px;">Twin-share</span>
  <span class="cell" style="left:514px;top:483px;">Bunk beds<br>Personal kitchen<br>locker</span>
  <span class="cell" style="left:623px;top:483px;">From $31 per<br>person per night</span>

  <span class="cell" style="left:405px;top:547px;">Double</span>
  <span class="cell" style="left:514px;top:547px;">Double bed<br>Personal kitchen<br>locker</span>
  <span class="cell" style="left:623px;top:547px;">From $31 per<br>person per night</span>

  <span class="cell" style="left:405px;top:611px;">Triple</span>
  <span class="cell" style="left:514px;top:611px;">Bunk bed and<br>single bed<br>Personal kitchen<br>locker</span>
  <span class="cell" style="left:623px;top:611px;">From $30 per<br>person per night</span>

  <span class="cell" style="left:405px;top:691px;">Quad</span>
  <span class="cell" style="left:514px;top:691px;">Bunk beds<br>Personal kitchen<br>locker</span>
  <span class="cell" style="left:623px;top:691px;">From $29 per<br>person per night</span>

  <!-- Facilities panel -->
  <h1 class="abs heading heading-main" style="left:783px;top:72px;width:310px;white-space:nowrap;">Hostel facilities &amp; local features</h1>
  <span class="flourish" style="left:893px;top:106px;" role="img" aria-label="Decorative flourish"></span>
  <p class="abs lead" style="left:783px;top:131px;width:312px;">Palm Rest Lodging Tidecourt proudly offers a range of facilities to all of our guests and a location that enables you to enjoy all that Saltmere has to offer with a minimum of hassle</p>
  <div class="rule-strong" style="left:783px;top:207px;width:310px;"></div>

  <ul class="features">
    <li>Free computer and Wi-Fi Internet access</li>
    <li>Fully-equipped kitchen</li>
    <li>On-site laundry facilities</li>
    <li>Private kitchen lockers</li>
    <li>Free access to gym equipment</li>
    <li>Air-conditioned dorm rooms</li>
    <li>Large open common areas</li>
    <li>Free off-street parking</li>
    <li>Free luggage storage service</li>
    <li>Free pickup service from the Roadkestrel and Staveline bus terminals, Corvel Island ferry terminal, and train station<sup>*</sup></li>
    <li>A short 200 metre walk to the beach, The Parade and Tallis Gardens</li>
    <li>Within 10 minutes walk to Saltmere’s pub and club precinct</li>
    <li>Next door to a shopping centre</li>
    <li>Located on central bus routes</li>
    <li>Gorgeous views of Murrow Knoll</li>
  </ul>

  <p class="note" style="left:783px;top:548px;width:310px;"><sup>*</sup> An airport pick-up and drop-off service is also available for $10 per<br>&nbsp;&nbsp;person one way</p>
</main>
</body>
</html>
```